Window Cleaning Flyer targeting Shopfronts and Small Commercial Work

Single page flyer similar to the flyer targeting small commercial work and shopfronts

Please include the following text:

Brisk Pane Services delivers high quality service to suburbs all around Melbourne. From Frankston to Kalkallo, Brisk has you covered!

With over 10 years experience, Brisk specialises in providing:
- Window Cleaning: via elevated work platforms, rope access and extension poles
- Pressure Cleaning: Including chlorine treatment to prevent mould regrowth on concrete area
- Roof Gutter Cleaning: using our ladder free gutter vacuum

We pride ourselves on neat and professional presentation and vast geographical reach across Melbourne.

Our services can be completed on a frequency that meets your window cleaning needs. Whether a weekly clean or a yearly service.

Brisk Pane Services Melbourne takes care of all your window cleaning needs.

Contact Us now for free quote!

Target Market(s)

Small business and commercial building owners

Industry/Entity Type

Window Cleaning

Requirements
Must have
• Only use photos/logos provided
Should not have
• Stock phots

```html
<!DOCTYPE html>
<html lang="en">
<head>
<meta charset="utf-8">
<title>Brisk Pane Services – Flyer</title>
<link href="https://fonts.googleapis.com/css2?family=Montserrat:wght@300;400;500;600;700;800;900&display=swap" rel="stylesheet">
<style>
  :root {
    --navy: #0f4f86;
    --yellow: #fff200;
    --ink: #2b2b2b;
    --white: #ffffff;
    --paper-light: #f6f6f6;
    --paper-dark: #dcdcdc;
  }
  * { box-sizing: border-box; margin: 0; padding: 0; }
  html, body { width: 927px; height: 1200px; overflow: hidden; }
  body { font-family: "Montserrat", Arial, sans-serif; color: var(--ink); }

  .flyer {
    position: relative;
    width: 927px;
    height: 1200px;
    overflow: hidden;
    background: radial-gradient(ellipse at 60% 40%, var(--paper-light) 0%, #ececec 55%, var(--paper-dark) 100%);
  }
  .artwork { position: absolute; inset: 0; }

  .brand-name {
    position: absolute;
    top: 58px; left: 662px;
    width: 230px;
    color: var(--navy);
    font-weight: 800;
    line-height: 1;
    text-align: center;
  }
  .brand-name .brand-main { display: block; font-size: 58px; letter-spacing: 1px; }
  .brand-name .brand-sub { display: block; font-size: 18px; letter-spacing: 0.5px; margin-top: 6px; }

  .headline {
    position: absolute;
    top: 196px; left: 28px;
    font-weight: 900;
    text-transform: uppercase;
    line-height: 0.9;
    color: var(--white);
  }
  .headline .hl-brand { display: block; font-size: 62px; color: var(--yellow); }
  .headline .hl-name { display: block; font-size: 62px; }
  .headline .hl-services { display: block; font-size: 38px; margin-top: 4px; }
  .headline .hl-delivers { display: block; font-size: 34px; }

  .tagline {
    position: absolute;
    top: 390px; left: 28px;
    color: var(--white);
    font-weight: 300;
    font-size: 27px;
    line-height: 36px;
    text-transform: uppercase;
    letter-spacing: -0.5px;
  }
  .tagline strong { font-weight: 700; }

  .coverage {
    position: absolute;
    top: 798px; left: 26px;
    color: var(--navy);
    font-size: 25px;
    font-weight: 700;
    line-height: 29px;
  }

  .experience {
    position: absolute;
    top: 876px; left: 0;
    width: 382px; height: 80px;
    background: var(--yellow);
    padding: 12px 0 0 30px;
    font-size: 21px;
    line-height: 26px;
    color: var(--ink);
    transform: rotate(-0.6deg);
  }
  .experience strong { font-weight: 700; }

  .service-list {
    position: absolute;
    top: 976px; left: 26px;
    width: 410px;
    list-style: none;
    font-size: 17px;
    line-height: 23px;
  }
  .service-list li { position: relative; padding-left: 26px; margin-bottom: 13px; }
  .service-list .tick { position: absolute; left: 0; top: 5px; }
  .service-list strong { color: var(--navy); font-weight: 700; }

  .divider {
    position: absolute;
    left: 464px; top: 848px;
    width: 1px; height: 276px;
    background: #b9b9b9;
  }

  .about {
    position: absolute;
    top: 796px; left: 506px;
    width: 390px;
    font-size: 17px;
    line-height: 24px;
  }
  .about p + p { margin-top: 12px; }
  .about strong { color: var(--navy); font-weight: 700; }

  .cta {
    position: absolute;
    top: 1004px; left: 506px;
    width: 382px; height: 52px;
    background: var(--yellow);
    font-size: 20px;
    line-height: 52px;
    text-align: center;
    transform: rotate(-0.6deg);
  }
  .cta strong { font-weight: 700; }

  .contact { position: absolute; top: 1064px; left: 538px; }
  .contact-row { display: flex; align-items: center; gap: 18px; color: var(--ink); }
  .contact-row svg { flex: none; }
  .contact-phone { font-size: 34px; font-weight: 700; letter-spacing: 2px; height: 46px; }
  .contact-line { font-size: 18px; letter-spacing: 1.5px; height: 27px; }

  .edge-yellow { position: absolute; left: 889px; top: 592px; width: 38px; height: 104px; background: var(--yellow); }
  .edge-navy { position: absolute; left: 889px; top: 704px; width: 38px; height: 52px; background: var(--navy); }
  .footer-band { position: absolute; left: 0; bottom: 0; width: 927px; height: 28px; background: var(--yellow); }
</style>
</head>
<body>
<main class="flyer">

  <svg class="artwork" width="927" height="1200" viewBox="0 0 927 1200">
    <defs>
      <linearGradient id="heroTone" x1="0" y1="0" x2="0.3" y2="1">
        <stop offset="0" stop-color="#9aa3ab"/>
        <stop offset="0.55" stop-color="#5f7487"/>
        <stop offset="1" stop-color="#2f577c"/>
      </linearGradient>
      <linearGradient id="houseTone" x1="0" y1="0" x2="0" y2="1">
        <stop offset="0" stop-color="#8aa07a"/>
        <stop offset="0.35" stop-color="#5a4638"/>
        <stop offset="0.6" stop-color="#3f8c82"/>
        <stop offset="1" stop-color="#8a5a44"/>
      </linearGradient>
      <linearGradient id="liftTone" x1="0" y1="0" x2="1" y2="1">
        <stop offset="0" stop-color="#b5563a"/>
        <stop offset="0.55" stop-color="#7d4a36"/>
        <stop offset="1" stop-color="#6e9a54"/>
      </linearGradient>
    </defs>

    <path role="img" aria-label="Photo: window cleaner using an extension pole on a modern slatted building facade"
          d="M0 0 H645 C 670 260 560 560 300 680 C 200 716 90 712 0 702 Z" fill="url(#heroTone)"/>

    <g role="img" aria-label="Photo: technician cleaning the windows of a two-storey timber house with a water-fed pole">
      <circle cx="662" cy="464" r="248" fill="#ffffff"/>
      <circle cx="662" cy="464" r="240" fill="url(#houseTone)"/>
    </g>

    <g role="img" aria-label="Photo: worker on an elevated work platform cleaning windows of a brick commercial building">
      <circle cx="416" cy="652" r="148" fill="#ffffff"/>
      <circle cx="416" cy="652" r="140" fill="url(#liftTone)"/>
    </g>
  </svg>

  <div class="brand-name">
    <span class="brand-main">BRISK</span>
    <span class="brand-sub">PANE SERVICES</span>
  </div>

  <h1 class="headline">
    <span class="hl-brand">Brisk</span>
    <span class="hl-name">Pane</span>
    <span class="hl-services">Services</span>
    <span class="hl-delivers">Delivers</span>
  </h1>

  <p class="tagline">High quality<br>service to<br>suburbs<br>all around<br><strong>Melbourne.</strong></p>

  <div class="edge-yellow"></div>
  <div class="edge-navy"></div>

  <h2 class="coverage">From Frankston to Kalkallo,<br>Brisk has you covered!</h2>

  <p class="experience">With over <strong>10 years experience</strong><br>Brisk specialises in providing:</p>

  <ul class="service-list">
    <li>
      <svg class="tick" width="18" height="16" viewBox="0 0 18 16"><path d="M2 9 L7 14 L16 2" fill="none" stroke="#0f4f86" stroke-width="3" stroke-linecap="round" stroke-linejoin="round"/></svg>
      <strong>Window Cleaning:</strong> via elevated work platforms, rope access and extension poles
    </li>
    <li>
      <svg class="tick" width="18" height="16" viewBox="0 0 18 16"><path d="M2 9 L7 14 L16 2" fill="none" stroke="#0f4f86" stroke-width="3" stroke-linecap="round" stroke-linejoin="round"/></svg>
      <strong>Pressure Cleaning:</strong> Including chlorine treatment to prevent mould regrowth on concrete areas
    </li>
    <li>
      <svg class="tick" width="18" height="16" viewBox="0 0 18 16"><path d="M2 9 L7 14 L16 2" fill="none" stroke="#0f4f86" stroke-width="3" stroke-linecap="round" stroke-linejoin="round"/></svg>
      <strong>Roof Gutter Cleaning:</strong> using our ladder free gutter vacuum
    </li>
  </ul>

  <div class="divider"></div>

  <div class="about">
    <p>We pride ourselves on our professional presentation and vast geographical reach across <strong>Melbourne.</strong></p>
    <p>Our services can be completed at a frequency that meets your window cleaning needs, from a weekly to yearly basis.</p>
  </div>

  <p class="cta"><strong>Contact Us</strong> now for <strong>free quote!</strong></p>

  <div class="contact">
    <div class="contact-row contact-phone">
      <svg width="10" height="16" viewBox="0 0 10 16"><rect x="1" y="1" width="8" height="14" rx="1.5" fill="none" stroke="#0f4f86" stroke-width="1.6"/><rect x="3" y="3" width="4" height="5" fill="#0f4f86"/></svg>
      <span>(03) 9000 4217</span>
    </div>
    <div class="contact-row contact-line">
      <svg width="12" height="10" viewBox="0 0 12 10"><rect x="0.5" y="0.5" width="11" height="9" fill="#0f4f86"/><path d="M0.5 0.5 L6 5.5 L11.5 0.5" fill="none" stroke="#ffffff" stroke-width="1"/></svg>
      <span>admin@briskpaneservices.com.au</span>
    </div>
    <div class="contact-row contact-line">
      <svg width="12" height="12" viewBox="0 0 12 12"><circle cx="6" cy="6" r="5.3" fill="none" stroke="#0f4f86" stroke-width="1.2"/><ellipse cx="6" cy="6" rx="2.3" ry="5.3" fill="none" stroke="#0f4f86" stroke-width="1"/><path d="M0.7 6 H11.3" stroke="#0f4f86" stroke-width="1"/></svg>
      <span>www.briskpaneservices.com.au</span>
    </div>
  </div>

  <div class="footer-band"></div>
</main>
</body>
</html>
```